Larkmoor Dental Center Specials/Offers

Take the advertisement pic (LABELED ADVERTISEMENT) and make it look "professional in appearance" using the logo and color scheme of Larkmoor Dental Center. The Phone number should be 614-382-2096. I want the same content, different background, professional looking document. I want it to be a 12"x12" document. High resolution files should include .PDF, .JPG and .AI. Any or all documents can be used for colors and overall scheme. I would like to have the overall colors include the main blue color from the file 4db749b4ef4c5e0717512bf7eb26bf54 and include the brown "swoosh" somewhere through/on the final document. Stock files of smiling young families can be used but not required. I am on a tight time-line and have placed 5 days as the deadline, but I will pick my favorite in as little as 2-3 days if I can get a good product. Again ALL the info from the Advertisement document should be included on the final product. Use any or all of the uploaded files for assistance. You can also visit our website for more info: www.larkmoordentalcenter.example Thanks

```html
<!DOCTYPE html>
<html lang="en">
<head>
<meta charset="utf-8">
<title>Larkmoor Dental Center – Specials &amp; Offers</title>
<link href="https://fonts.googleapis.com/css2?family=Fira+Sans:wght@300;400;600;700&display=swap" rel="stylesheet">
<style>
  :root {
    --canvas-bg: #e9e7e4;
    --paper: #f4f4f4;
    --blue-deep: #274e61;
    --blue-main: #2f5b70;
    --blue-glow: #607f8c;
    --band-blue: #2c586d;
    --brown: #5b4741;
    --logo-blue: #3d6478;
    --text-light: #ffffff;
    --text-soft: #dfe8ec;
    --text-muted: #b9cbd3;
  }
  * { box-sizing: border-box; margin: 0; padding: 0; }
  html, body {
    width: 1200px; height: 953px; overflow: hidden;
    background: var(--canvas-bg);
    font-family: "Fira Sans", Arial, sans-serif;
  }
  .flyer {
    position: absolute; left: 143px; top: 20px;
    width: 913px; height: 913px;
    background: var(--paper);
    overflow: hidden;
    color: var(--text-light);
  }
  .flyer-bg { position: absolute; inset: 0; }
  .family-photo {
    position: absolute; left: 420px; top: 0; width: 493px; height: 250px;
    background: linear-gradient(160deg, #d7d2cc 0%, #b9a493 40%, #6d6f75 75%, #4a4d55 100%);
  }
  .brand {
    position: absolute; left: 40px; top: 140px; width: 370px;
  }
  .brand-row { display: flex; align-items: center; gap: 10px; }
  .brand-mark { width: 32px; height: 32px; border-radius: 50%; background: var(--logo-blue); flex: none; }
  .brand-name {
    font-size: 24px; font-weight: 600; color: var(--logo-blue);
    white-space: nowrap; line-height: 1.1;
  }
  .brand-services {
    margin: 6px 0 0 42px; font-size: 12px; letter-spacing: 1.5px;
    color: var(--brown); white-space: nowrap; line-height: 1.2;
  }
  .tagline {
    position: absolute; left: 40px; top: 222px; width: 340px;
    text-align: center; font-size: 24px; color: var(--logo-blue); line-height: 1.15;
  }
  .tagline strong { font-weight: 700; }
  .offer { position: absolute; text-align: center; }
  .offer-title { font-weight: 700; font-size: 30px; }
  .offer-line { font-weight: 300; font-size: 27px; color: var(--text-soft); line-height: 1.2; }
  .fine-print { font-size: 12px; color: var(--text-muted); margin-top: 4px; }
  .offer-exam { left: 40px; top: 395px; width: 400px; }
  .offer-referral { left: 40px; top: 585px; width: 400px; }
  .offer-referral .offer-line { font-size: 31px; color: var(--text-light); }
  .offer-bleach { left: 40px; top: 715px; width: 400px; }
  .providers { left: 470px; top: 270px; width: 400px; }
  .providers .offer-title { font-size: 27px; }
  .provider-list { font-size: 20px; line-height: 1.3; letter-spacing: .5px; margin-top: 4px; }
  .offer-discount { left: 470px; top: 470px; width: 400px; }
  .offer-discount .offer-title { font-size: 44px; }
  .offer-discount .offer-line { font-size: 29px; color: var(--text-light); font-weight: 400; }
  .contact-band {
    position: absolute; left: 0; bottom: 0; width: 100%; height: 125px;
    display: flex; align-items: center; justify-content: space-between;
    padding: 0 48px;
  }
  .call-text { font-size: 20px; font-weight: 700; letter-spacing: .8px; }
  .web-text { font-size: 20px; font-weight: 400; margin-top: 4px; letter-spacing: .4px; }
  .phone { font-size: 56px; font-weight: 600; letter-spacing: 1px; }
</style>
</head>
<body>
  <main class="flyer">
    <svg class="flyer-bg" width="913" height="913" viewBox="0 0 913 913" aria-hidden="true">
      <defs>
        <radialGradient id="panelGlow" cx="0.45" cy="0.5" r="0.6">
          <stop offset="0" stop-color="#607f8c"/>
          <stop offset="0.6" stop-color="#2f5b70"/>
          <stop offset="1" stop-color="#274e61"/>
        </radialGradient>
      </defs>
      <path d="M0 330 C 220 330, 420 300, 560 250 S 800 160, 913 150 L 913 913 L 0 913 Z" fill="var(--brown)"/>
      <path d="M0 352 C 230 352, 430 322, 570 272 S 800 182, 913 172 L 913 913 L 0 913 Z" fill="url(#panelGlow)"/>
      <rect x="0" y="788" width="913" height="125" fill="var(--band-blue)"/>
    </svg>

    <div class="family-photo" role="img" aria-label="Photo of a smiling young family: mother, father and son"></div>

    <div class="brand">
      <div class="brand-row">
        <span class="brand-mark"></span>
        <span class="brand-name">Larkmoor Dental Center</span>
      </div>
      <div class="brand-services">FAMILY · COSMETIC · IMPLANTS</div>
    </div>
    <p class="tagline">Where the <strong>Whole Family</strong><br>can be seen!</p>

    <section class="offer offer-exam">
      <p class="offer-title">$59 New patients X-Rays</p>
      <p class="offer-line">Comprehensive Exam</p>
      <p class="offer-line">Regular Cleaning</p>
      <p class="fine-print">*Only patients without Dental Benefits</p>
    </section>

    <section class="offer offer-referral">
      <p class="offer-line">Ask about our<br>Referral Program</p>
    </section>

    <section class="offer offer-bleach">
      <p class="offer-title">$99 Bleaching Special</p>
    </section>

    <section class="offer providers">
      <p class="offer-title">Preferred provider for:</p>
      <p class="provider-list">NORTHGATE DENTAL, VERIDIAN LIFE,<br>CORVANE, ALTURA HEALTH,<br>BLUECREST AND<br>UNIFIED HARBOR</p>
      <p class="fine-print">We take all other non-IMO plans</p>
    </section>

    <section class="offer offer-discount">
      <p class="offer-title">20% OFF</p>
      <p class="offer-line">treatment scheduled<br>on your first visit</p>
      <p class="fine-print">Only paitents without Dental Benefits</p>
    </section>

    <footer class="contact-band">
      <div>
        <p class="call-text">CALL TODAY FOR AN APPOINTMENT</p>
        <p class="web-text">www.larkmoordentalcenter.example</p>
      </div>
      <p class="phone">614-382-2096</p>
    </footer>
  </main>
</body>
</html>
```